Powerpoint template for Trivia Company

Revamp of our current powerpoint template to make it more professional and fun for the players. Something worthy of a trivia company. Please see logo attached for potential colour - but also open to other ideas.

NO BRANDING REQUIRED (IE: No mention of our company or logo on the template please)

Target Market(s)

Bars/restaurants

Colors
3176b5
00a990

```html
<!DOCTYPE html>
<html lang="en">
<head>
<meta charset="utf-8">
<title>First Category: General Knowledge</title>
<link rel="stylesheet" href="https://fonts.googleapis.com/css2?family=Londrina+Solid:wght@400;900&display=swap">
<style>
  :root {
    --navy-deep: #070a3a;
    --indigo: #26248a;
    --violet: #3a3db5;
    --teal: #3bb9b4;
    --teal-mid: #2592ad;
    --white: #ffffff;
    --yellow: #ffcc00;
    --shadow: rgba(10, 10, 60, 0.55);
  }
  html, body {
    margin: 0;
    padding: 0;
    width: 1200px;
    height: 675px;
    overflow: hidden;
    background: var(--navy-deep);
  }
  .slide {
    position: relative;
    width: 1200px;
    height: 675px;
    overflow: hidden;
    font-family: "Londrina Solid", "Arial Black", sans-serif;
  }
  .backdrop {
    position: absolute;
    inset: 0;
    background:
      radial-gradient(ellipse 48% 42% at 38% 48%, var(--teal) 0%, var(--teal-mid) 45%, transparent 80%),
      radial-gradient(ellipse 70% 70% at 50% 52%, var(--violet) 0%, var(--indigo) 55%, var(--navy-deep) 100%);
  }
  .heading {
    position: absolute;
    left: 0;
    width: 100%;
    margin: 0;
    text-align: center;
    line-height: 1;
    font-weight: 900;
    text-transform: uppercase;
    paint-order: stroke fill;
  }
  .heading--category {
    top: 148px;
    left: 47px;
    font-size: 116px;
    letter-spacing: 1px;
    color: var(--white);
    text-shadow: 3px 4px 0 var(--shadow);
  }
  .heading--topic {
    top: 293px;
    font-size: 124px;
    letter-spacing: 1px;
    color: var(--yellow);
    -webkit-text-stroke: 8px var(--white);
    text-shadow: 4px 5px 0 var(--shadow);
  }
  .book-icon {
    position: absolute;
    left: 487px;
    top: 456px;
    width: 216px;
    height: 154px;
  }
</style>
</head>
<body>
  <main class="slide">
    <div class="backdrop" role="img" aria-label="Abstract flowing waves in deep navy, indigo and teal with floating wireframe gems"></div>
    <h1 class="heading heading--category">First Category:</h1>
    <h2 class="heading heading--topic">General Knowledge</h2>
    <svg class="book-icon" viewBox="0 0 216 154" aria-hidden="true">
      <g fill="none" stroke="var(--white)" stroke-width="9" stroke-linejoin="round" stroke-linecap="round">
        <path d="M108 34 C86 14 50 8 28 12 V128 C52 124 86 128 108 146 C130 128 164 124 188 128 V12 C166 8 130 14 108 34 Z"/>
        <path d="M108 34 V146"/>
        <path d="M20 28 H8 V146 H92 C98 146 102 150 108 150 C114 150 118 146 124 146 H208 V28 H196"/>
      </g>
    </svg>
  </main>
</body>
</html>
```